Email Sig, Letterhead, Business Card Design

Need a stationary package including email signature, letterhead/envelope, and business card design incorporating our new logo.

```html
<!DOCTYPE html>
<html lang="en">
<head>
<meta charset="utf-8">
<title>Kestrel Engineering – Business Card</title>
<link rel="stylesheet" href="https://fonts.googleapis.com/css2?family=Montserrat:wght@500;600;700&family=Open+Sans:wght@400;600&display=swap">
<style>
  :root {
    --bg: #141414;
    --card: #1f1f20;
    --card-edge: #d2421a;
    --orange: #ee6a2c;
    --blue: #1f6fb8;
    --text: #e9e9e9;
    --rule: #5a5a5c;
    --pattern-light: #3a3a3b;
    --pattern-dark: #202021;
  }
  * { box-sizing: border-box; margin: 0; padding: 0; }
  html, body { width: 1200px; height: 884px; overflow: hidden; background: var(--bg); }
  body {
    display: flex; flex-direction: column; align-items: center; justify-content: center;
    gap: 44px; font-family: "Open Sans", sans-serif;
  }

  .card {
    position: relative;
    width: 620px;
    height: 354px;
    background: linear-gradient(135deg, #232324, var(--card) 60%, #1b1b1c);
    border-bottom: 3px solid var(--card-edge);
    border-left: 2px solid var(--card-edge);
    box-shadow: 0 16px 40px rgba(0,0,0,.6);
    overflow: hidden;
  }

  /* Wordmark block (shared) */
  .wordmark { text-align: center; }
  .wordmark-name {
    font-family: "Montserrat", sans-serif;
    font-weight: 700;
    font-size: 22px;
    letter-spacing: .5px;
    color: var(--orange);
    line-height: 1;
    white-space: nowrap;
  }
  .wordmark-details {
    margin-top: 4px;
    font-family: "Montserrat", sans-serif;
    font-size: 7px;
    font-weight: 600;
    letter-spacing: .4px;
    color: var(--blue);
    text-transform: uppercase;
    border-bottom: 1px solid var(--orange);
    padding-bottom: 3px;
    line-height: 1.5;
    white-space: nowrap;
  }
  .wordmark-details .registration { color: var(--orange); letter-spacing: 1.6px; }

  /* Front */
  .card-front .brand { position: absolute; right: 44px; top: 34px; width: 280px; }
  .brand-mark {
    width: 42px; height: 42px;
    margin: 0 auto 12px;
    border-radius: 50%;
    background: var(--blue);
  }
  .card-divider {
    position: absolute;
    left: 44px; right: 40px;
    top: 196px;
    height: 1px;
    background: linear-gradient(90deg, transparent, var(--rule) 20%, #cfcfcf 55%, var(--rule) 85%, transparent);
  }
  .person { position: absolute; left: 44px; top: 128px; font-family: "Montserrat", sans-serif; }
  .person-name { font-size: 21px; font-weight: 700; color: var(--orange); letter-spacing: .4px; line-height: 1.1; }
  .person-title { font-size: 18px; font-weight: 600; color: var(--blue); line-height: 1.25; }

  .contact-list { position: absolute; left: 44px; top: 216px; list-style: none; }
  .contact-list li {
    display: flex; align-items: center; gap: 9px;
    font-size: 16px; color: var(--text); line-height: 1.6;
  }
  .contact-list svg { width: 15px; height: 15px; flex: none; }

  .office-address {
    position: absolute; right: 44px; top: 216px;
    text-align: right; font-size: 16px; color: var(--text); line-height: 1.6; font-style: normal;
  }
  .office-address .company { color: var(--orange); font-weight: 600; }

  /* Back */
  .back-pattern {
    position: absolute; inset: 0;
    background: linear-gradient(135deg, var(--pattern-light), var(--pattern-dark) 55%, #2a2a2b);
  }
  .card-back .wordmark { position: absolute; right: 40px; bottom: 34px; width: 280px; }
</style>
</head>
<body>
  <section class="card card-front">
    <div class="brand wordmark">
      <div class="brand-mark"></div>
      <div class="wordmark-name">KESTREL ENGINEERING</div>
      <div class="wordmark-details">
        <div>1450 Cedar Ridge Lane, Austin, Texas 78701</div>
        <div class="registration">State Firm Registration F-4418</div>
      </div>
    </div>

    <div class="person">
      <div class="person-name">MARTIN HALE</div>
      <div class="person-title">Managing Director</div>
    </div>

    <div class="card-divider"></div>

    <ul class="contact-list">
      <li>
        <svg viewBox="0 0 24 24" fill="var(--orange)"><path d="M6.6 10.8a15 15 0 0 0 6.6 6.6l2.2-2.2c.3-.3.7-.4 1-.2 1.1.4 2.3.6 3.6.6.6 0 1 .4 1 1V20c0 .6-.4 1-1 1A17 17 0 0 1 3 4c0-.6.4-1 1-1h3.5c.6 0 1 .4 1 1 0 1.3.2 2.5.6 3.6.1.3 0 .7-.2 1z"/></svg>
        +15550102233
      </li>
      <li>
        <svg viewBox="0 0 24 24"><rect x="2" y="5" width="20" height="14" rx="1" fill="var(--orange)"/><path d="M2 6l10 7 10-7" fill="none" stroke="var(--card)" stroke-width="1.6"/></svg>
        info@kestrelengineering.com
      </li>
      <li>
        <svg viewBox="0 0 24 24" fill="none" stroke="var(--orange)" stroke-width="2"><circle cx="12" cy="12" r="9"/><path d="M3 12h18M12 3c3 3 3 15 0 18M12 3c-3 3-3 15 0 18"/></svg>
        www.kestrelengineering.com
      </li>
    </ul>

    <address class="office-address">
      <div class="company">Kestrel Engineering Ltd.</div>
      <div>48 Harbor View Road</div>
      <div>Oakville, ON L6J 3K2</div>
    </address>
  </section>

  <section class="card card-back">
    <div class="back-pattern" role="img" aria-label="Repeating embossed logo pattern covering the back of the card"></div>
    <div class="wordmark">
      <div class="wordmark-name">KESTREL ENGINEERING</div>
      <div class="wordmark-details">
        <div>1450 Cedar Ridge Lane, Austin, Texas 78701</div>
        <div class="registration">State Firm Registration F-4418</div>
      </div>
    </div>
  </section>
</body>
</html>
```